The Corwell Laundromat - Pre-Opening Marketing Postcard

We need a design for a 6"x11" postcard that we will use to advertise the upcoming opening of a new laundromat in Ashby Glen. The name of the store is "The Corwell Laundromat", and the most important things are: match the colors on the card to our logo colors, but also add in some yellow and possibly red accents; say "Free Dryers" in a big, obvious way; include generic washer/dryer pictures, put a basic map of the location on the back of the card, and leave the right 1/3 of the card blank except for the retail indicia and the name "Local Postal Customer". Please refer to the uploaded file showing an example basic layout for the card.
Target Market(s)
low-to-middle-income residents within a 3-mile radius
Industry/Entity Type
Retail
Requirements
Must have
- - The words FREE DRYERS!
- - A simple, hand-drawn map of the location (412 Tansley Road, Ashby Glen) and major roads nearby (hollis avenue, tansley road, fenwick ave, etc.)
- - The words Opening Soon! (or Opening in March!)
- - The words Newly-Built Laundromat, or New Store!, or something similar
- - The words Local Postal Customer on the back, as shown in my example design layout
- - The retail indicia positioned as shown in my example design layout
- - nothing else on the rear, right-hand 1/3 of the card other than local postal customer and the indicia
Nice to have
- - A transparent background using the generic washers and/or generic dryers pictures
- - Some yellow and red accents or colors to appeal to our hispanic customers
- - The words Professional Wash & Fold Service
Should not have
- - Anything on the back, right-hand 1/3 of the card other than Local Postal Customer and the retail indicia picture

```html
<!DOCTYPE html>
<html lang="en">
<head>
<meta charset="utf-8">
<title>The Corwell Laundromat – Pre-Opening Postcard</title>
<link rel="stylesheet" href="https://fonts.googleapis.com/css2?family=Oswald:wght@500;600&family=Open+Sans:wght@700;800&display=swap">
<style>
  :root {
    --page: #ebebea;
    --navy: #123f8c;
    --royal: #0a62b0;
    --sky: #29b4ea;
    --red: #e41e26;
    --yellow: #f8ec28;
    --teal-pale: #b9dcd9;
    --ink: #1b1b1b;
    --white: #ffffff;
    --steel-light: #d4d6d8;
    --steel-dark: #7d8287;
    --map: #e9eaec;
  }
  html, body {
    margin: 0;
    width: 1124px;
    height: 1200px;
    overflow: hidden;
    background: var(--page);
  }
  .card {
    position: absolute;
    left: 62px;
    width: 1000px;
    height: 556px;
    box-shadow: 0 4px 14px rgba(0,0,0,.22);
    background: var(--white);
  }
  .card--front { top: 36px; }
  .card--back { top: 608px; }
  .card svg { display: block; width: 100%; height: 100%; }
  .display { font-family: "Oswald", "Arial Narrow", sans-serif; font-weight: 600; }
  .body-bold { font-family: "Open Sans", Arial, sans-serif; font-weight: 700; }
  .postal { font-family: Arial, Helvetica, sans-serif; }
</style>
</head>
<body>

<svg width="0" height="0" style="position:absolute">
  <defs>
    <symbol id="starburst" viewBox="-100 -100 200 200">
      <polygon points="100,0 88,18 92,38 75,50 71,71 50,75 38,92 18,88 0,100 -18,88 -38,92 -50,75 -71,71 -75,50 -92,38 -88,18 -100,0 -88,-18 -92,-38 -75,-50 -71,-71 -50,-75 -38,-92 -18,-88 0,-100 18,-88 38,-92 50,-75 71,-71 75,-50 92,-38 88,-18" fill="var(--white)"/>
      <polygon transform="scale(0.92)" points="100,0 88,18 92,38 75,50 71,71 50,75 38,92 18,88 0,100 -18,88 -38,92 -50,75 -71,71 -75,50 -92,38 -88,18 -100,0 -88,-18 -92,-38 -75,-50 -71,-71 -50,-75 -38,-92 -18,-88 0,-100 18,-88 38,-92 50,-75 71,-71 75,-50 92,-38 88,-18" fill="var(--yellow)"/>
    </symbol>
    <symbol id="pin" viewBox="0 0 20 28">
      <path d="M10 0C4.5 0 0 4.4 0 9.8 0 17 10 28 10 28s10-11 10-18.2C20 4.4 15.5 0 10 0z" fill="var(--red)"/>
      <circle cx="10" cy="9.8" r="3.8" fill="var(--white)"/>
    </symbol>
    <linearGradient id="steel" x1="0" y1="0" x2="1" y2="0.3">
      <stop offset="0" stop-color="var(--steel-dark)"/>
      <stop offset="0.5" stop-color="var(--steel-light)"/>
      <stop offset="1" stop-color="#9ea2a6"/>
    </linearGradient>
    <linearGradient id="header-blue" x1="0" y1="0" x2="1" y2="0">
      <stop offset="0" stop-color="var(--sky)"/>
      <stop offset="0.55" stop-color="var(--royal)"/>
      <stop offset="1" stop-color="var(--navy)"/>
    </linearGradient>
    <linearGradient id="address-bar" x1="0" y1="0" x2="1" y2="0">
      <stop offset="0" stop-color="#ffffff"/>
      <stop offset="1" stop-color="#d9dadc"/>
    </linearGradient>
    <linearGradient id="footer-fade" x1="0" y1="0" x2="1" y2="0">
      <stop offset="0" stop-color="#ffffff"/>
      <stop offset="1" stop-color="#d8d9db"/>
    </linearGradient>
  </defs>
</svg>

<!-- Front -->
<section class="card card--front" aria-label="Postcard front">
  <svg viewBox="0 0 1125 625">
    <rect class="footer" width="1125" height="625" fill="url(#footer-fade)"/>
    <rect class="photo" width="1125" height="560" fill="url(#steel)" role="img" aria-label="Photo of a row of stainless steel front-loading laundromat washers"/>
    <path class="swoosh swoosh--sky" d="M0 360 C300 250 700 380 860 450 C960 490 1060 470 1125 425 L1125 500 C1060 530 960 540 860 510 C700 450 300 320 0 430 Z" fill="var(--sky)"/>
    <path class="swoosh swoosh--navy" d="M0 385 C300 285 700 400 860 470 C960 510 1060 500 1125 470 L1125 525 C1060 545 960 550 860 530 C700 470 300 340 0 445 Z" fill="var(--navy)"/>
    <path class="white-field" d="M0 430 C300 330 700 450 860 515 C960 550 1060 545 1125 520 L1125 625 L0 625 Z" fill="url(#footer-fade)"/>

    <g class="ribbon">
      <path d="M830 0 H1085 V270 L957 340 L830 270 Z" fill="var(--white)"/>
      <path d="M842 0 H1073 V262 L957 326 L842 262 Z" fill="var(--red)"/>
      <text class="display" x="957" y="75" font-size="44" fill="var(--yellow)" text-anchor="middle">FREE</text>
      <text class="display" x="957" y="135" font-size="62" fill="var(--yellow)" text-anchor="middle">DRYERS</text>
      <text x="957" y="176" font-size="20" fill="var(--white)" text-anchor="middle">★</text>
      <text class="display" x="957" y="225" font-size="38" fill="var(--white)" text-anchor="middle">OPENING</text>
      <text class="display" x="957" y="258" font-size="27" fill="var(--white)" text-anchor="middle">IN MARCH!</text>
    </g>

    <g class="badge">
      <use href="#starburst" x="755" y="345" width="190" height="190"/>
      <text class="display" x="848" y="427" font-size="38" fill="var(--red)" text-anchor="middle">NEW</text>
      <text class="display" x="850" y="473" font-size="38" fill="var(--red)" text-anchor="middle">STORE!</text>
    </g>

    <g class="brand">
      <circle cx="272" cy="356" r="172" fill="var(--white)"/>
      <circle cx="272" cy="356" r="163" fill="var(--teal-pale)"/>
      <text class="body-bold" x="272" y="340" font-size="40" fill="var(--navy)" text-anchor="middle">The Corwell</text>
      <text class="body-bold" x="272" y="395" font-size="40" fill="var(--navy)" text-anchor="middle">Laundromat</text>
    </g>

    <use href="#pin" x="70" y="572" width="20" height="28"/>
    <text class="body-bold" x="104" y="596" font-size="23" fill="var(--ink)">412 Tansley Road, Ashby Glen</text>
    <text class="body-bold" x="1095" y="594" font-size="32.5" fill="var(--ink)" text-anchor="end">Professional Wash &amp; Fold Service</text>
  </svg>
</section>

<!-- Back -->
<section class="card card--back" aria-label="Postcard back">
  <svg viewBox="0 0 1125 625">
    <rect width="1125" height="625" fill="var(--white)"/>
    <path class="edge edge--sky" d="M0 0 H705 C745 70 725 210 625 335 C545 435 520 525 545 625 H0 Z" fill="var(--sky)"/>
    <path class="edge edge--navy" d="M0 0 H690 C730 65 710 205 612 330 C532 430 505 522 528 625 H0 Z" fill="var(--royal)"/>
    <path class="edge edge--white" d="M0 0 H672 C712 62 692 200 596 325 C516 425 490 520 510 625 H0 Z" fill="var(--white)"/>
    <path class="header" d="M0 0 H660 C700 60 690 190 640 278 H0 Z" fill="url(#header-blue)"/>

    <path class="map" d="M0 278 H636 C560 380 512 460 505 536 H0 Z" fill="var(--map)" role="img" aria-label="Simple street map around 412 Tansley Road, Ashby Glen, showing Tansley Road and Hollis Avenue with a location pin"/>

    <rect class="address-bar" x="0" y="536" width="510" height="62" fill="url(#address-bar)"/>
    <rect class="base-strip" x="0" y="598" width="520" height="27" fill="var(--sky)"/>
    <use href="#pin" x="26" y="554" width="20" height="28"/>
    <text class="body-bold" x="64" y="580" font-size="27" fill="var(--ink)">412 Tansley Road, Ashby Glen</text>

    <text class="display" x="240" y="88" font-size="58" fill="var(--yellow)" text-anchor="middle">FREE</text>
    <text class="display" x="240" y="172" font-size="84" fill="var(--yellow)" text-anchor="middle">DRYERS</text>

    <path class="ribbon-bar" d="M0 205 H435 A30 30 0 0 1 465 235 V248 A30 30 0 0 1 435 278 H0 Z" fill="var(--red)"/>
    <text class="display" x="33" y="262" font-size="48" fill="var(--white)">OPENING IN MARCH!</text>

    <g class="brand">
      <circle cx="598" cy="168" r="128" fill="var(--white)"/>
      <circle cx="598" cy="168" r="120" fill="var(--teal-pale)"/>
      <text class="body-bold" x="598" y="160" font-size="30" fill="var(--navy)" text-anchor="middle">The Corwell</text>
      <text class="body-bold" x="598" y="202" font-size="30" fill="var(--navy)" text-anchor="middle">Laundromat</text>
    </g>

    <g class="badge">
      <use href="#starburst" x="568" y="418" width="178" height="178"/>
      <text class="display" x="651" y="498" font-size="38" fill="var(--red)" text-anchor="middle">NEW</text>
      <text class="display" x="653" y="543" font-size="38" fill="var(--red)" text-anchor="middle">STORE!</text>
    </g>

    <g class="indicia">
      <rect x="1014" y="30" width="90" height="88" fill="none" stroke="var(--ink)" stroke-width="1"/>
      <text class="postal" x="1059" y="50" font-size="12" fill="var(--ink)" text-anchor="middle">PRSRT STD</text>
      <text class="postal" x="1059" y="64" font-size="12" fill="var(--ink)" text-anchor="middle">ECRWSS</text>
      <text class="postal" x="1059" y="78" font-size="12" fill="var(--ink)" text-anchor="middle">U.S. POSTAGE</text>
      <text class="postal" x="1059" y="92" font-size="12" font-weight="700" fill="var(--ink)" text-anchor="middle">PAID</text>
      <text class="postal" x="1059" y="106" font-size="12" fill="var(--ink)" text-anchor="middle">EDDM RETAIL</text>
    </g>

    <g class="mailing">
      <rect x="790" y="197" width="314" height="109" fill="none" stroke="var(--ink)" stroke-width="1"/>
      <text class="postal" x="1080" y="222" font-size="13" fill="var(--ink)" text-anchor="end">*****************ECRWSS****</text>
      <text class="postal" x="813" y="266" font-size="17" fill="var(--ink)">Local</text>
      <text class="postal" x="813" y="284" font-size="17" fill="var(--ink)">Postal Customer</text>
    </g>
  </svg>
</section>

</body>
</html>
```